Merry Fern Lumo alcohol cooler

I need a design using my Merry Fern Beverage Logo for 4 different styles of Malt Beverage. The cocktails are easy drinking tropical feel. We will be using the best ingredients and try to be all natural and organic.
Zaller Lime
Zaller Orange
Zaller Grapefruit
Zaller Strawberry
We would like as few colors as possible in the design.

Target Market(s)

21 - 50
Women

Requirements
Must have
• the 4 styles
• my LOGO
• label dimension inside 3"wide x 4"high maximum
• 4 pack design
• label must have 12 FL OZ
• label must have 5% ALC/VOL
Nice to have
• Clean crisp feel
Should not have
• please keep design to 3 colors or less

```html
<!DOCTYPE html>
<html lang="en">
<head>
<meta charset="utf-8">
<title>Merry Fern Beverage – Zaller Coolers</title>
<link rel="stylesheet" href="https://fonts.googleapis.com/css2?family=Arimo:wght@700&family=Libre+Baskerville&display=swap">
<style>
  :root {
    --brand-green: #1a5538;
    --paper: #ffffff;
    --lime-liquid: #d4e592;
    --lime-ink: #a3bb28;
    --strawberry-liquid: #f5abb2;
    --strawberry-ink: #e4344f;
    --grapefruit-liquid: #ecdac6;
    --grapefruit-ink: #ef735e;
    --orange-liquid: #e8b42c;
    --orange-ink: #f0521a;
  }
  * { box-sizing: border-box; margin: 0; padding: 0; }
  html, body { width: 1200px; height: 1000px; overflow: hidden; background: var(--paper); }
  .lineup { position: relative; width: 1200px; height: 1000px; }
  .bottle { position: absolute; top: 22px; width: 210px; height: 810px; }
  .bottle svg { position: absolute; inset: 0; }
  .bottle--lime { left: 120px; --liquid: var(--lime-liquid); --ink: var(--lime-ink); }
  .bottle--strawberry { left: 370px; --liquid: var(--strawberry-liquid); --ink: var(--strawberry-ink); }
  .bottle--grapefruit { left: 620px; --liquid: var(--grapefruit-liquid); --ink: var(--grapefruit-ink); }
  .bottle--orange { left: 870px; --liquid: var(--orange-liquid); --ink: var(--orange-ink); }
  .glass { fill: var(--liquid); }
  .cap, .neck-ribbon { fill: var(--brand-green); }
  .label { position: absolute; left: 26px; top: 366px; width: 158px; text-align: center; }
  .brand-seal {
    width: 142px; height: 142px; margin: 0 auto; border-radius: 50%;
    background: var(--brand-green); display: flex; align-items: center; justify-content: center;
    color: var(--paper); font-family: "Arimo", sans-serif; font-weight: 700;
    font-size: 15px; line-height: 1.3; letter-spacing: 1px; text-transform: uppercase;
  }
  .flavour {
    margin-top: 10px; font-family: "Libre Baskerville", serif; font-size: 27px;
    line-height: 36px; color: var(--ink); letter-spacing: -0.5px; white-space: nowrap;
  }
  .flavour-name { display: block; }
  .rules { margin: 10px 6px 0; }
  .rules span { display: block; height: 8px; border-bottom: 3px dotted var(--brand-green); }
  .facts {
    display: flex; justify-content: space-between; margin: 14px 4px 0;
    font-family: "Arimo", sans-serif; font-size: 9px; color: #1d1d1d;
  }
  .facts .abv { color: var(--brand-green); }
</style>
</head>
<body>
<main class="lineup">

  <article class="bottle bottle--lime">
    <svg viewBox="0 0 210 810" aria-hidden="true">
      <path class="glass" d="M78 40 L132 40 C134 150 138 230 150 270 C165 310 206 320 208 360 L208 780 C208 800 198 806 180 806 L30 806 C12 806 2 800 2 780 L2 360 C4 320 45 310 60 270 C72 230 76 150 78 40 Z"/>
      <rect class="cap" x="72" y="8" width="66" height="30" rx="6"/>
      <path class="neck-ribbon" d="M84 12 H126 V212 L105 192 L84 212 Z"/>
    </svg>
    <div class="label">
      <div class="brand-seal">Merry Fern<br>Beverage</div>
      <h2 class="flavour"><span class="flavour-name">Zaller</span><span class="flavour-name">Lime</span></h2>
      <div class="rules"><span></span><span></span><span></span></div>
      <p class="facts"><span>12 fl. oz</span><span class="abv">5% Alc / Vol</span></p>
    </div>
  </article>

  <article class="bottle bottle--strawberry">
    <svg viewBox="0 0 210 810" aria-hidden="true">
      <path class="glass" d="M78 40 L132 40 C134 150 138 230 150 270 C165 310 206 320 208 360 L208 780 C208 800 198 806 180 806 L30 806 C12 806 2 800 2 780 L2 360 C4 320 45 310 60 270 C72 230 76 150 78 40 Z"/>
      <rect class="cap" x="72" y="8" width="66" height="30" rx="6"/>
      <path class="neck-ribbon" d="M84 12 H126 V212 L105 192 L84 212 Z"/>
    </svg>
    <div class="label">
      <div class="brand-seal">Merry Fern<br>Beverage</div>
      <h2 class="flavour"><span class="flavour-name">Zaller</span><span class="flavour-name">Strawberry</span></h2>
      <div class="rules"><span></span><span></span><span></span></div>
      <p class="facts"><span>12 fl. oz</span><span class="abv">5% Alc / Vol</span></p>
    </div>
  </article>

  <article class="bottle bottle--grapefruit">
    <svg viewBox="0 0 210 810" aria-hidden="true">
      <path class="glass" d="M78 40 L132 40 C134 150 138 230 150 270 C165 310 206 320 208 360 L208 780 C208 800 198 806 180 806 L30 806 C12 806 2 800 2 780 L2 360 C4 320 45 310 60 270 C72 230 76 150 78 40 Z"/>
      <rect class="cap" x="72" y="8" width="66" height="30" rx="6"/>
      <path class="neck-ribbon" d="M84 12 H126 V212 L105 192 L84 212 Z"/>
    </svg>
    <div class="label">
      <div class="brand-seal">Merry Fern<br>Beverage</div>
      <h2 class="flavour"><span class="flavour-name">Zaller</span><span class="flavour-name">Grapefruit</span></h2>
      <div class="rules"><span></span><span></span><span></span></div>
      <p class="facts"><span>12 fl. oz</span><span class="abv">5% Alc / Vol</span></p>
    </div>
  </article>

  <article class="bottle bottle--orange">
    <svg viewBox="0 0 210 810" aria-hidden="true">
      <path class="glass" d="M78 40 L132 40 C134 150 138 230 150 270 C165 310 206 320 208 360 L208 780 C208 800 198 806 180 806 L30 806 C12 806 2 800 2 780 L2 360 C4 320 45 310 60 270 C72 230 76 150 78 40 Z"/>
      <rect class="cap" x="72" y="8" width="66" height="30" rx="6"/>
      <path class="neck-ribbon" d="M84 12 H126 V212 L105 192 L84 212 Z"/>
    </svg>
    <div class="label">
      <div class="brand-seal">Merry Fern<br>Beverage</div>
      <h2 class="flavour"><span class="flavour-name">Zaller</span><span class="flavour-name">Orange</span></h2>
      <div class="rules"><span></span><span></span><span></span></div>
      <p class="facts"><span>12 fl. oz</span><span class="abv">5% Alc / Vol</span></p>
    </div>
  </article>

</main>
</body>
</html>
```